Social Media Graphics - ALL TEXT RK

We are looking for a series of social media graphics for Instagram (standard size 1:1 (1080x1080px) that are ALL TEXT. We want the following quotes below on each graphic; one quote per graphic. AND, In very small letters at the bottom of each graphic, add @RKMarlowLive

The look and feel of these graphics should be complimentary to the color palette attached below; but keep them simple. But the design is up to you; at the end of this document, I provided various samples of all text graphics that I like as examples.

Target Market(s)

women looking to lose weight

Industry/Entity Type

health and wellness

Colors
E54698
E96AAD
F1A4CE
F9D9EA
FCEFF6

Requirements
Must have
• the quotes in the document
Should not have
• no stock photography

```html
<!DOCTYPE html>
<html lang="en">
<head>
<meta charset="utf-8">
<title>Belly Fat Quote – RK</title>
<link href="https://fonts.googleapis.com/css2?family=Montserrat:wght@700;800&display=swap" rel="stylesheet">
<style>
  :root {
    --pink-deep: #E54698;
    --pink-mid: #E96AAD;
    --pink-soft: #F1A4CE;
    --pink-pale: #F9D9EA;
    --pink-mist: #FCEFF6;
    --white: #FFFFFF;
  }
  html, body {
    margin: 0;
    padding: 0;
    width: 1200px;
    height: 1200px;
    overflow: hidden;
  }
  .post {
    position: relative;
    width: 1200px;
    height: 1200px;
    background: var(--pink-soft);
    font-family: "Montserrat", sans-serif;
  }
  .speech-bubble {
    position: absolute;
    inset: 0;
    width: 1200px;
    height: 1200px;
  }
  .bubble-outline {
    fill: var(--pink-soft);
    stroke: var(--pink-deep);
    stroke-width: 12;
    stroke-linejoin: round;
  }
  .bubble-card {
    fill: var(--pink-mist);
  }
  .quote {
    position: absolute;
    left: 209px;
    top: 336px;
    width: 820px;
    margin: 0;
    font-size: 56px;
    font-weight: 700;
    line-height: 61px;
    color: var(--pink-deep);
  }
  .handle {
    position: absolute;
    left: 0;
    right: 0;
    top: 1116px;
    margin: 0;
    text-align: center;
    font-size: 38px;
    font-weight: 800;
    color: var(--white);
    line-height: 46px;
  }
</style>
</head>
<body>
  <main class="post">
    <svg class="speech-bubble" viewBox="0 0 1080 1080" aria-hidden="true">
      <defs>
        <filter id="card-shadow" x="-5%" y="-5%" width="110%" height="115%">
          <feDropShadow dx="0" dy="3" stdDeviation="4" flood-color="#B0306F" flood-opacity="0.25"/>
        </filter>
      </defs>
      <path class="bubble-outline"
        d="M155,192 H925 Q1000,192 1000,267 V710 Q1000,785 925,785 H895
           Q885,855 862,878 Q846,892 828,876 L730,785 H155
           Q80,785 80,710 V267 Q80,192 155,192 Z"/>
      <g filter="url(#card-shadow)">
        <rect class="bubble-card" x="120" y="233" width="838" height="512" rx="22"/>
        <path class="bubble-card" d="M740,740 L838,842 Q848,852 852,838 Q870,790 878,740 Z"/>
      </g>
    </svg>

    <p class="quote">Frustrated with belly<br>fat that won't budge?<br>I've got the solution<br>that finally worked for<br>me-no crazy diets.<br>required.</p>

    <p class="handle">@RKMarlowLive</p>
  </main>
</body>
</html>
```